11 x 11 Flyer Design for Social Media - Reverse Mortgages

62 or older?

A Reverse Mortgage
could be
Your Road to Financial Freedom

* No Monthly Payments
* No Income Requirements
* No Credit Score Requirements
* No Loss of Ownership

Receive cash by lump sum, monthly installments or a line of credit!!

Call us today for a Free Consultation!!
(800) 647-2915

Harborline Financial Services, Inc.
NMLS #517830
www.harborlinefunds.example

```html
<!DOCTYPE html>
<html lang="en">
<head>
<meta charset="utf-8">
<title>Reverse Mortgages – Harborline Financial Services</title>
<link href="https://fonts.googleapis.com/css2?family=Archivo+Black&family=Roboto:wght@400;500;700;900&display=swap" rel="stylesheet">
<style>
  :root {
    --blue: #0560a6;
    --gold: #a8982e;
    --ink: #3a3536;
    --white: #ffffff;
    --sky-top: #c9ced3;
    --sky-low: #eef0f2;
  }
  * { box-sizing: border-box; margin: 0; padding: 0; }
  html, body { width: 1200px; height: 1200px; overflow: hidden; background: var(--white); }
  body { font-family: "Roboto", Arial, sans-serif; }
  .flyer { position: relative; width: 1200px; height: 1200px; overflow: hidden; background: var(--white); }

  .hero-photo {
    position: absolute; left: 0; top: 0; width: 1200px; height: 650px;
    background:
      radial-gradient(ellipse 420px 520px at 300px 460px, #8a6a55 0%, #b9a89c 35%, rgba(240,240,240,0) 70%),
      linear-gradient(180deg, var(--sky-top) 0%, #d8dde1 45%, var(--sky-low) 80%, #f7f7f7 100%);
  }

  .headline { position: absolute; left: 640px; top: 196px; width: 520px; }
  .age-question {
    font-weight: 900; font-size: 32px; line-height: 1; color: var(--blue);
    margin-bottom: 12px;
  }
  .headline-title {
    font-family: "Archivo Black", "Arial Black", sans-serif;
    font-weight: 400; color: var(--gold); line-height: 1;
  }
  .headline-title .line-1 { display: block; font-size: 90px; letter-spacing: 1px; }
  .headline-title .line-2 { display: block; font-size: 50px; letter-spacing: 6.5px; margin-top: 6px; }
  .tagline {
    margin-top: 14px;
    font-weight: 900; font-size: 23.5px; color: var(--ink); letter-spacing: 0.3px;
  }

  .benefits-band {
    position: absolute; left: 0; top: 650px; width: 1200px; height: 233px;
    background: var(--blue); color: var(--white);
  }
  .benefits { position: absolute; left: 40px; top: 42px; list-style: none; }
  .benefits li {
    display: flex; align-items: center; gap: 14px;
    font-weight: 500; font-size: 30px; height: 41.5px;
  }
  .benefits svg { width: 26px; height: 26px; flex: none; }

  .payout { position: absolute; left: 624px; top: 22px; width: 500px; }
  .payout-pill {
    position: absolute; left: 40px; top: 18px; width: 459px; height: 51px;
    background: var(--gold); border-radius: 26px;
    font-weight: 700; font-size: 27px; line-height: 51px; padding-left: 104px; color: var(--white);
  }
  .payout-icon {
    position: absolute; left: 0; top: 0; width: 86px; height: 86px;
    border-radius: 50%; background: var(--white);
  }
  .payout-options {
    position: absolute; left: 0; top: 100px; width: 528px; text-align: center;
    font-weight: 700; font-size: 41px; line-height: 44px;
  }
  .payout-options .or { color: var(--gold); }

  .company-name {
    position: absolute; left: 56px; top: 990px; width: 330px;
    display: flex; align-items: center; gap: 14px;
    font-weight: 700; font-size: 26px; line-height: 1.2; color: var(--blue);
  }
  .company-name .dot { width: 40px; height: 40px; border-radius: 50%; background: var(--gold); flex: none; }

  .cta-pill {
    position: absolute; left: 617px; top: 922px; width: 511px; height: 51px;
    background: var(--gold); border-radius: 26px; color: var(--white);
    font-size: 22px; line-height: 51px; text-align: center;
  }
  .cta-pill strong { font-weight: 900; letter-spacing: 0.5px; }
  .phone-line { position: absolute; left: 605px; top: 996px; display: flex; align-items: center; gap: 20px; }
  .phone-number { font-weight: 900; font-size: 64px; color: var(--blue); line-height: 1; letter-spacing: -1px; }
  .web-line { position: absolute; left: 610px; top: 1064px; display: flex; align-items: center; gap: 22px; }
  .web-address { font-weight: 900; font-size: 32px; color: var(--gold); }

  .footer-line {
    position: absolute; left: 0; top: 1144px; width: 1200px;
    font-weight: 700; font-size: 21.5px; color: var(--ink);
    display: flex; justify-content: center; align-items: center; gap: 6px;
  }
  .footer-line .firm { color: var(--blue); }
</style>
</head>
<body>
<main class="flyer">
  <div class="hero-photo" role="img" aria-label="Smiling senior couple in white shirts on a soft beach with sky and sea behind them"></div>

  <section class="headline">
    <p class="age-question">62 or older?</p>
    <h1 class="headline-title"><span class="line-1">REVERSE</span><span class="line-2">MORTGAGES</span></h1>
    <p class="tagline">YOUR ROAD TO FINANCIAL FREEDOM</p>
  </section>

  <section class="benefits-band">
    <ul class="benefits">
      <li><svg viewBox="0 0 26 26"><circle cx="13" cy="13" r="13" fill="var(--gold)"/><path d="M8 13.5l3.5 3.5 6.5-7" fill="none" stroke="var(--blue)" stroke-width="2.6" stroke-linecap="round" stroke-linejoin="round"/></svg>No Monthly Payments</li>
      <li><svg viewBox="0 0 26 26"><circle cx="13" cy="13" r="13" fill="var(--gold)"/><path d="M8 13.5l3.5 3.5 6.5-7" fill="none" stroke="var(--blue)" stroke-width="2.6" stroke-linecap="round" stroke-linejoin="round"/></svg>No Income Requirements</li>
      <li><svg viewBox="0 0 26 26"><circle cx="13" cy="13" r="13" fill="var(--gold)"/><path d="M8 13.5l3.5 3.5 6.5-7" fill="none" stroke="var(--blue)" stroke-width="2.6" stroke-linecap="round" stroke-linejoin="round"/></svg>No Credit Score Requirements</li>
      <li><svg viewBox="0 0 26 26"><circle cx="13" cy="13" r="13" fill="var(--gold)"/><path d="M8 13.5l3.5 3.5 6.5-7" fill="none" stroke="var(--blue)" stroke-width="2.6" stroke-linecap="round" stroke-linejoin="round"/></svg>No Loss of Ownership</li>
    </ul>

    <div class="payout">
      <div class="payout-pill">Receive cash by lump sum</div>
      <svg class="payout-icon" viewBox="0 0 86 86" aria-hidden="true">
        <circle cx="43" cy="43" r="43" fill="var(--white)"/>
        <text x="43" y="55" text-anchor="middle" font-family="Roboto, Arial, sans-serif" font-weight="900" font-size="34" fill="var(--blue)">$</text>
      </svg>
      <p class="payout-options">Monthly Installments<br><span class="or">or</span> A line of credit!!</p>
    </div>
  </section>

  <div class="company-name"><span class="dot"></span><span>Harborline Financial Services, Inc.</span></div>

  <div class="cta-pill">Call us today for a <strong>FREE CONSULTATION!</strong></div>
  <div class="phone-line">
    <svg width="58" height="60" viewBox="0 0 58 60" aria-hidden="true">
      <path d="M14 4 L24 16 L18 24 C22 33 27 38 36 42 L44 36 L56 46 L50 56 C28 58 4 34 4 12 Z" fill="var(--blue)"/>
      <path d="M30 14 A14 14 0 0 1 44 28" fill="none" stroke="var(--gold)" stroke-width="4" stroke-linecap="round"/>
      <path d="M31 4 A24 24 0 0 1 54 27" fill="none" stroke="var(--blue)" stroke-width="4" stroke-linecap="round"/>
    </svg>
    <span class="phone-number">(800) 647-2915</span>
  </div>
  <div class="web-line">
    <svg width="50" height="50" viewBox="0 0 50 50" aria-hidden="true">
      <g stroke="var(--blue)" stroke-width="3" stroke-linecap="round">
        <line x1="14" y1="2" x2="14" y2="10"/><line x1="2" y1="14" x2="10" y2="14"/>
        <line x1="5" y1="5" x2="9" y2="9"/><line x1="23" y1="5" x2="19" y2="9"/><line x1="5" y1="23" x2="9" y2="19"/>
      </g>
      <path d="M16 16 L46 28 L34 32 L44 42 L40 46 L30 36 L26 46 Z" fill="var(--blue)"/>
    </svg>
    <span class="web-address">www.harborlinefunds.example</span>
  </div>

  <p class="footer-line">
    <span class="firm">Harborline Financial Services, Inc.</span>
    <span>| NMLS #517830 |</span>
    <svg width="16" height="22" viewBox="0 0 16 22" aria-hidden="true"><path d="M8 1 A7 7 0 0 1 15 8 C15 13 8 21 8 21 C8 21 1 13 1 8 A7 7 0 0 1 8 1 Z" fill="var(--gold)"/><circle cx="8" cy="8" r="2.6" fill="var(--white)"/></svg>
    <span>4180 Quarry Bend Rd, Ashford Mills, MD 21900</span>
  </p>
</main>
</body>
</html>
```